Banner Ad Design Project

I place ads in Clickreach and also get traffic from sites like http://www.holisticcarelist.com.au/ to offer our free meditation CD and report at http://quietpathstudio.com.au/get-the-free-meditation-cd
We need new designs to improve this campaign.
Target Market(s)
40+ year old women, looking for personal growth or help with stress, depression, anxiety, sleep problems, health issues, memory/concentration issues
Industry/Entity Type
Campaign

```html
<!DOCTYPE html>
<html lang="en">
<head>
<meta charset="utf-8">
<title>Free Meditation CD – Banner Set</title>
<link rel="stylesheet" href="https://fonts.googleapis.com/css2?family=Fira+Sans:ital,wght@0,500;0,600;1,600&family=Mulish:wght@800&display=swap">
<style>
  :root {
    --stage: #464343;
    --sun: #f2c500;
    --sun-soft: rgba(242, 197, 0, 0.88);
    --leaf: #5ba51c;
    --navy: #1e3799;
    --olive: #4d4636;
    --paper: #ffffff;
    --photo-a: #c9c27a;
    --photo-b: #6f8a3a;
    --photo-c: #e6d9c6;
    --disc-a: #dfe8f4;
  }
  * { box-sizing: border-box; margin: 0; padding: 0; }
  html, body { width: 1200px; height: 900px; overflow: hidden; background: var(--stage); }
  body { position: relative; font-family: "Fira Sans", "Trebuchet MS", sans-serif; }

  .banner { position: absolute; overflow: hidden; background: var(--paper); }
  .banner svg.art { position: absolute; inset: 0; width: 100%; height: 100%; }
  .banner > p { position: absolute; white-space: nowrap; }

  .offer { color: var(--navy); font-weight: 600; line-height: 1.08; letter-spacing: -0.2px; }
  .offer .free { color: var(--leaf); font-style: italic; font-weight: 500; }
  .quote { color: var(--olive); font-style: italic; font-weight: 600; line-height: 1.2; }
  .value { color: var(--navy); font-weight: 600; }
  .cta { font-family: "Mulish", "Century Gothic", sans-serif; font-weight: 800; color: var(--navy); line-height: 1.0; }
  .stock { color: var(--olive); font-weight: 500; }

  /* square */
  .square { left: 180px; top: 131px; width: 358px; height: 298px; }
  .square .offer { left: 15px; top: 30px; font-size: 23px; }
  .square .offer .free { font-size: 25px; display: block; margin-bottom: 2px; }
  .square .quote { left: 18px; top: 122px; font-size: 14px; }
  .square .value { left: 138px; top: 170px; font-size: 14px; }
  .square .cta { left: 14px; top: 252px; font-size: 23px; }
  .square .stock { left: 76px; top: 279px; font-size: 13px; }

  /* small leaderboard */
  .strip { left: 180px; top: 499px; width: 559px; height: 71px; }
  .strip .offer { left: 12px; top: 7px; font-size: 18px; line-height: 1.3; }
  .strip .value { left: 164px; top: 52px; font-size: 12px; }
  .strip .cta { left: 448px; top: 8px; font-size: 17px; line-height: 1.05; }
  .strip .stock { left: 464px; top: 53px; font-size: 11px; letter-spacing: -0.1px; }

  /* large leaderboard */
  .wide { left: 180px; top: 610px; width: 670px; height: 119px; }
  .wide .offer { left: 12px; top: 11px; font-size: 26px; line-height: 1.1; }
  .wide .quote { left: 12px; top: 72px; font-size: 14px; }
  .wide .value { left: 218px; top: 90px; font-size: 14px; }
  .wide .cta { left: 576px; top: 10px; font-size: 21px; line-height: 1.0; }
  .wide .stock { left: 597px; top: 78px; font-size: 13px; line-height: 1.15; }

  /* skyscraper */
  .tower { left: 886px; top: 91px; width: 191px; height: 719px; }
  .tower .offer { left: 14px; top: 43px; font-size: 25px; line-height: 1.14; letter-spacing: -0.4px; }
  .tower .offer .free { font-size: 27px; display: block; }
  .tower .quote { left: 14px; top: 181px; font-size: 15px; }
  .tower .value { left: 110px; top: 259px; font-size: 14px; }
  .tower .cta { left: 14px; top: 647px; font-size: 25px; }
  .tower .stock { left: 50px; top: 700px; font-size: 14px; }
</style>
</head>
<body>

<section class="banner square" aria-label="Free meditation CD offer, square">
  <svg class="art" viewBox="0 0 358 298">
    <defs>
      <linearGradient id="photoSq" x1="0" y1="0" x2="1" y2="1">
        <stop offset="0" stop-color="var(--photo-a)"/>
        <stop offset="0.5" stop-color="var(--photo-c)"/>
        <stop offset="1" stop-color="var(--photo-b)"/>
      </linearGradient>
    </defs>
    <rect width="358" height="298" fill="url(#photoSq)" role="img" aria-label="Photo of a woman with headphones relaxing on the grass"/>
    <rect x="0" y="23" width="211" height="170" fill="var(--sun-soft)"/>
    <path d="M0 204 C 110 240, 240 256, 358 246 L358 298 L0 298 Z" fill="var(--paper)"/>
    <path d="M0 204 C 110 240, 240 256, 358 246" fill="none" stroke="var(--navy)" stroke-width="5"/>
    <circle cx="300" cy="235" r="58" fill="var(--disc-a)" role="img" aria-label="Meditation CD disc"/>
  </svg>
  <p class="offer"><span class="free">FREE</span>Meditation CD &amp;<br>Special Report...</p>
  <p class="quote">“How to Meditate Deeper<br>&nbsp;Than a Zen Monk!”</p>
  <p class="value">$37 value</p>
  <p class="cta">→ Get Yours Now</p>
  <p class="stock">While stocks last</p>
</section>

<section class="banner strip" aria-label="Free meditation CD offer, small leaderboard">
  <svg class="art" viewBox="0 0 559 71">
    <defs>
      <linearGradient id="photoStrip" x1="0" y1="0" x2="1" y2="0">
        <stop offset="0" stop-color="var(--photo-b)"/>
        <stop offset="0.5" stop-color="var(--photo-c)"/>
        <stop offset="1" stop-color="var(--photo-a)"/>
      </linearGradient>
    </defs>
    <rect x="0" y="0" width="222" height="71" fill="var(--sun)"/>
    <rect x="222" y="0" width="222" height="71" fill="url(#photoStrip)" role="img" aria-label="Photo of a woman with headphones relaxing on the grass"/>
    <path d="M432 0 C 446 24, 446 48, 440 71" fill="none" stroke="var(--navy)" stroke-width="4"/>
    <circle cx="395" cy="36" r="34" fill="var(--disc-a)" role="img" aria-label="Meditation CD disc"/>
  </svg>
  <p class="offer"><span class="free">FREE</span> Meditation CD<br>and Special Report</p>
  <p class="value">$37 value</p>
  <p class="cta">→ Get<br>&nbsp;&nbsp;Yours Now</p>
  <p class="stock">While stocks last</p>
</section>

<section class="banner wide" aria-label="Free meditation CD offer, leaderboard">
  <svg class="art" viewBox="0 0 670 119">
    <defs>
      <linearGradient id="photoWide" x1="0" y1="0" x2="1" y2="0">
        <stop offset="0" stop-color="var(--photo-b)"/>
        <stop offset="0.5" stop-color="var(--photo-c)"/>
        <stop offset="1" stop-color="var(--photo-a)"/>
      </linearGradient>
    </defs>
    <rect x="0" y="0" width="290" height="119" fill="var(--sun)"/>
    <rect x="290" y="0" width="280" height="119" fill="url(#photoWide)" role="img" aria-label="Photo of a woman with headphones relaxing on the grass"/>
    <path d="M555 0 C 576 38, 576 80, 566 119" fill="none" stroke="var(--navy)" stroke-width="5"/>
    <circle cx="532" cy="71" r="40" fill="var(--disc-a)" role="img" aria-label="Meditation CD disc"/>
  </svg>
  <p class="offer"><span class="free">FREE</span> Meditation CD<br>and Special Report...</p>
  <p class="quote">“How to Meditate Deeper<br>&nbsp;Than a Zen Monk!”</p>
  <p class="value">$37 value</p>
  <p class="cta">→ Get<br>&nbsp;&nbsp;&nbsp;Yours<br>&nbsp;&nbsp;&nbsp;Now</p>
  <p class="stock">While<br>stocks last</p>
</section>

<section class="banner tower" aria-label="Free meditation CD offer, skyscraper">
  <svg class="art" viewBox="0 0 191 719">
    <defs>
      <linearGradient id="photoTower" x1="0" y1="0" x2="0" y2="1">
        <stop offset="0" stop-color="var(--photo-a)"/>
        <stop offset="0.5" stop-color="var(--photo-c)"/>
        <stop offset="1" stop-color="var(--photo-b)"/>
      </linearGradient>
    </defs>
    <rect x="0" y="0" width="191" height="295" fill="var(--sun)"/>
    <rect x="0" y="295" width="191" height="350" fill="url(#photoTower)" role="img" aria-label="Photo of a woman with headphones resting her chin on her hands"/>
    <path d="M0 597 C 60 618, 130 636, 191 640 L191 719 L0 719 Z" fill="var(--paper)"/>
    <path d="M0 597 C 60 618, 130 636, 191 640" fill="none" stroke="var(--navy)" stroke-width="5"/>
    <circle cx="133" cy="588" r="54" fill="var(--disc-a)" role="img" aria-label="Meditation CD disc"/>
  </svg>
  <p class="offer"><span class="free">FREE</span>Meditation CD<br>and Special<br>Report...</p>
  <p class="quote">“How to Meditate<br>&nbsp;&nbsp;Deeper Than a<br>&nbsp;&nbsp;Zen Monk!”</p>
  <p class="value">$37 value</p>
  <p class="cta">→ Get Yours<br>&nbsp;&nbsp;&nbsp;&nbsp;Now</p>
  <p class="stock">While stocks last</p>
</section>

</body>
</html>
```